Professional and creatice Life Coach - Business Card design

I just relaunched my website and now i a need a correspoonding business card for my task as life coach. My website is www.tbalrond.com as reference. The compass is kind of a symbol for my work, as I help people navigate through their challenging phases in life. The business card should be colorful, but not too playful as I also adress business people. So it sould be creative, but professional (also to suport my other business as Management Consultant)

Target Market(s)

People who want to get teir problems resolved, in business, partnership and other personal realms

Industry/Entity Type

Life Coaching

Contact Information for Business Card

Front side should include Name, Phone number, Email, Website and address

Font styles to use
Sans Serif

Colors
add136

Requirements
Must have
• "Mag. Leopold Brantner" -> Name
"Energetische Praxis" -> Jobtitle (describing my profession as life coach)
colours and style should match my website www.tbalrond.com
Nice to have
• a compass as a symbol

```html
<!DOCTYPE html>
<html lang="de">
<head>
<meta charset="utf-8">
<title>Business Card – Leopold Brantner</title>
<link rel="stylesheet" href="https://fonts.googleapis.com/css2?family=Raleway:wght@500;700&family=Open+Sans:wght@400&display=swap">
<style>
  :root {
    --brand-blue: #4476bb;
    --card-white: #f7f8fa;
    --page-bg: #ffffff;
    --ink: #333b33;
    --rule: #3c4a3c;
    --on-blue: #ffffff;
  }
  * { margin: 0; padding: 0; box-sizing: border-box; }
  html, body {
    width: 1200px; height: 515px; overflow: hidden;
    background: var(--page-bg);
  }
  .canvas { position: relative; width: 1200px; height: 515px; }
  .card {
    position: absolute; top: 127px; width: 446px; height: 267px;
    box-shadow: 0 6px 18px rgba(0,0,0,0.18);
    overflow: hidden;
  }
  .card--front { left: 137px; background: var(--card-white); }
  .card--back  { left: 616px; background: var(--brand-blue); }

  .front-header {
    position: absolute; left: 0; top: 0; width: 100%; height: 90px;
    background: var(--brand-blue);
  }
  .accent-bar {
    position: absolute; left: 47px; top: 29px; width: 6px; height: 35px;
    background: var(--on-blue);
  }
  .holder-name {
    position: absolute; left: 65px; top: 30px;
    font-family: "Raleway", sans-serif; font-weight: 700;
    font-size: 16.5px; color: var(--on-blue); white-space: nowrap;
  }
  .holder-title {
    position: absolute; left: 65px; top: 52px;
    font-family: "Raleway", sans-serif; font-weight: 500;
    font-size: 11.5px; color: var(--on-blue); white-space: nowrap;
  }
  .contact-list {
    position: absolute; left: 50px; top: 126px; list-style: none;
    font-family: "Open Sans", sans-serif; font-size: 14px;
    line-height: 21.5px; color: var(--ink);
  }
  .contact-rule {
    position: absolute; left: 50px; top: 204px; width: 51px; height: 1.5px;
    background: var(--rule);
  }
  .address {
    position: absolute; left: 50px; top: 224px;
    font-family: "Open Sans", sans-serif; font-size: 13px;
    color: var(--ink); white-space: nowrap;
  }
  .brand-mark {
    position: absolute; display: flex; align-items: center; gap: 6px;
    font-family: "Raleway", sans-serif; font-weight: 700; white-space: nowrap;
  }
  .brand-mark--small {
    left: 343px; top: 194px; font-size: 12px; color: var(--brand-blue);
  }
  .brand-mark--small .brand-dot {
    width: 12px; height: 12px; border-radius: 50%; background: var(--brand-blue);
  }
  .brand-mark--large {
    left: 0; right: 0; top: 116px; justify-content: center;
    font-size: 24px; color: var(--on-blue); gap: 10px;
  }
  .brand-mark--large .brand-dot {
    width: 22px; height: 22px; border-radius: 50%; background: var(--on-blue);
  }
</style>
</head>
<body>
<main class="canvas">
  <section class="card card--front" aria-label="Vorderseite">
    <header class="front-header">
      <span class="accent-bar"></span>
      <h1 class="holder-name">Mag. Leopold Brantner</h1>
      <p class="holder-title">Energetische Praxis</p>
    </header>
    <ul class="contact-list">
      <li>+43 660 4817392</li>
      <li>leopold@brantner.co</li>
      <li>www.tbalrond.com</li>
    </ul>
    <span class="contact-rule"></span>
    <p class="address">Lindenweg 12, 5020 Salzburg, Austria</p>
    <div class="brand-mark brand-mark--small">
      <span class="brand-dot"></span><span>Brantner</span>
    </div>
  </section>

  <section class="card card--back" aria-label="Rückseite">
    <div class="brand-mark brand-mark--large">
      <span class="brand-dot"></span><span>Brantner</span>
    </div>
  </section>
</main>
</body>
</html>
```